Drifting Ages Chronicle - Book Cover Design

I need a cover (front, spine, back) designed for the second edition of the historical book - Drifting Ages Chronicle. This book was created to be a more engaging supplementary resource to the dry texts of most middle and high school social studies classrooms. Although comprehensive and exhaustively researched, the book at times uses humor and irony to engage the reader. The cover should reflect this tone.

Book Title: Drifting Ages Chronicle
Subtitle: The Tales, Traditions and Turning Points of World History and the Regional Challenges of Today
Author: Noel Wickstrom
Updates

Project Deadline Extended
Reason: As multiple designers are working on adjustments and I am looking for new, creative ideas, I am extending the deadline five days. Thank you.

Project Deadline Extended
Reason: Artists are still making alterations to suggestions made and I also want to give designers a chance to submit new ideas.

Target Market(s)

Middle School and High School Teachers

Font styles to use
Serif

Colors
ec1f27
ffffff
000000

Requirements
Must have
• 1) See attachment for text for front cover, spine, back cover
• 2) Central, engaging image
Nice to have
• A subtle hint of humor, light tone
• Potentially upside down globe spinning
• Prefer black, red, white color scheme
Should not have
• Cartoonish text, images

```html
<!DOCTYPE html>
<html lang="en">
<head>
<meta charset="utf-8">
<title>Drifting Ages Chronicle – Cover Spread</title>
<link rel="stylesheet" href="https://fonts.googleapis.com/css2?family=Signika:wght@400;600&family=Fira+Sans:wght@400;600&family=Cutive+Mono&display=swap">
<style>
  :root {
    --red: #ec1f27;
    --white: #ffffff;
    --black: #000000;
    --cover-dark: #232223;
    --back-dark: #121212;
    --strip: #1b1b1b;
    --band-text: #fff3a8;
    --body-text: #e6e6e6;
    --stage: #d6d6d6;
    --map-light: #c9a15a;
    --map-mid: #8a6a33;
    --map-dark: #3b2a14;
  }
  * { box-sizing: border-box; margin: 0; padding: 0; }
  html, body { width: 1200px; height: 850px; overflow: hidden; }
  body {
    background: var(--stage);
    display: flex; align-items: center; justify-content: center;
  }
  .cover-spread {
    width: 1120px; height: 722px;
    display: flex;
    box-shadow: 0 10px 30px rgba(0,0,0,.35);
  }

  /* Back cover */
  .back-cover {
    width: 482px; height: 100%;
    position: relative;
    background: var(--back-dark);
    padding: 88px 48px 0 53px;
    color: var(--body-text);
    font-family: "Fira Sans", sans-serif;
    overflow: hidden;
  }
  .back-cover .backdrop {
    position: absolute; left: 0; right: 0; bottom: 0; height: 330px;
    background: linear-gradient(to bottom, rgba(18,18,18,1) 0%, #2a2a2a 35%, #3d3d3d 100%);
  }
  .back-cover .content { position: relative; z-index: 1; }
  .back-heading {
    font-weight: 600; font-size: 13.5px; color: var(--white);
    margin-bottom: 24px;
  }
  .back-copy p {
    font-size: 10.6px; line-height: 1.42; text-align: justify;
    margin-bottom: 16px;
  }
  .back-quote {
    margin-top: 42px;
    font-size: 10.6px; line-height: 1.42; text-align: justify;
  }

  /* Spine */
  .spine {
    width: 159px; height: 100%;
    background: var(--cover-dark);
    position: relative;
  }
  .spine-title, .spine-author {
    position: absolute; white-space: nowrap;
    transform: rotate(-90deg); transform-origin: left top;
  }
  .spine-title {
    left: 38px; top: 580px;
    font-family: "Signika", sans-serif; font-size: 33px; color: var(--white);
  }
  .spine-author {
    left: 108px; top: 518px;
    font-family: "Cutive Mono", monospace; font-size: 24px;
    letter-spacing: 10px; color: var(--red);
  }
  .spine-edition {
    position: absolute; left: 0; right: 0; bottom: 42px;
    text-align: center; color: var(--red); font-family: "Signika", sans-serif;
  }
  .spine-edition .num { display: block; font-size: 48px; font-weight: 600; line-height: 1; }
  .spine-edition .word { display: block; font-size: 20px; }

  /* Front cover */
  .front-cover {
    width: 479px; height: 100%;
    background: var(--cover-dark);
    position: relative;
    display: flex; flex-direction: column;
  }
  .front-title {
    font-family: "Signika", sans-serif; font-size: 31px; color: var(--white);
    text-align: center; margin-top: 50px; letter-spacing: .3px;
  }
  .front-edition {
    text-align: center; color: var(--red); font-family: "Signika", sans-serif;
    margin-top: 26px;
  }
  .front-edition .num { display: block; font-size: 64px; font-weight: 600; line-height: .9; }
  .front-edition .word { display: block; font-size: 27px; line-height: 1.1; }
  .subtitle-band {
    background: var(--red);
    height: 62px; margin-top: 8px;
    display: flex; align-items: center; justify-content: center;
    text-align: center; color: var(--band-text);
    font-family: "Fira Sans", sans-serif; font-size: 15.5px; line-height: 1.35;
    padding: 0 30px;
  }
  .cover-art {
    flex: 1;
    background:
      radial-gradient(circle at 18% 78%, var(--map-light) 0%, var(--map-mid) 22%, transparent 38%),
      radial-gradient(ellipse at 60% 40%, var(--map-light) 0%, var(--map-mid) 45%, var(--map-dark) 100%);
  }
  .author-strip {
    height: 82px; background: var(--strip);
    display: flex; align-items: center; justify-content: center;
    font-family: "Cutive Mono", monospace; font-size: 24px;
    letter-spacing: 9px; color: var(--white);
  }
</style>
</head>
<body>
  <div class="cover-spread">
    <section class="back-cover">
      <div class="backdrop" role="img" aria-label="Faint photograph of ancient arched ruins"></div>
      <div class="content">
        <h2 class="back-heading">Do you know how we got to here?</h2>
        <div class="back-copy">
          <p>Well, if you're like 97.4% of the people walking the planet, you haven't got a clue. Sure, you might know a bit about a couple rivers in Mesopotamia, how Theron wandered around Athens asking questions or how Mattis Lund got ticked off one day and nailed a really long essay to the door of a church. But to be honest (and don't be embarrassed), you've got some gaps.</p>
          <p>Be dense no more. In Drifting Ages Chronicle, Noel Wickstrom once again takes you through all the major tales, traditions and turning points of world history – not just European history, but WORLD history. You'll figure out real quick that the West might have had some crowning moments, but for the whole of human history, it's been the Persians, the Indians, the Chinese, the Muslims or some horse peoples from the steppe that have truly turned us into the clever little creatures we are today.</p>
          <p>And while most world history books fade off once the Cold War comes to a close, this sometimes sardonic tome just gets going. Updated to include contemporary debates over topics such as Brexit, the rise of ISIS, claims to the South China Sea, the mounting refugee crisis and the controversial presidency of Dane Rowley, this second edition finishes with a distinctively comprehensive look at the 21st century challenges facing nine major regions of today's world – Africa, Latin America, Japan, China, the Middle East, India, Russia, Europe and the United States.</p>
        </div>
        <p class="back-quote">"Noel Wickstrom expertly understands what his audience wants to know, what they need to know. A page-turning account of our proudest achievements and our most colossal bumblings. It's world history for the rest of us." – Ida Marren</p>
      </div>
    </section>

    <section class="spine">
      <span class="spine-title">DRIFTING AGES CHRONICLE</span>
      <span class="spine-author">NOEL WICKSTROM</span>
      <div class="spine-edition"><span class="num">2</span><span class="word">EDITION</span></div>
    </section>

    <section class="front-cover">
      <h1 class="front-title">DRIFTING AGES CHRONICLE</h1>
      <div class="front-edition"><span class="num">2</span><span class="word">EDITION</span></div>
      <div class="subtitle-band">The tales, traditions and turning points of world history and the regional challenges of today</div>
      <div class="cover-art" role="img" aria-label="Antique sepia world map with a brass compass in the lower left"></div>
      <div class="author-strip">NOEL WICKSTROM</div>
    </section>
  </div>
</body>
</html>
```